We need a striking new book cover for a new book.

This book presents a modern concept based on the latest discoveries in the field of molecular genetics and nuclear physics. It helps us to understand the direction in which the universe, the world and each of us as individuals could be heading given the impact of laws of physics and evolution.

Book Title: The Gradual Compass
Author: Radosław Piętek

The text to go on the front cover is as follows :

The Gradual Compass
Radosław Piętek
is a scientist, author, publisher and a member of LUMIO

The photograph of the author uploaded should go on the back cover.
The text to go on the back cover is as follows:

This book presents a modern concept based on the latest discoveries in the field of molecular genetics and nuclear physics. It helps us to understand the direction in which the universe, the world, and each of us as individuals could be heading, given the impact of the laws of physics, and evolution. Entropy (law of physics) implies increasing chaos and that our universe inclines towards ever greater disorder.
Evolution means that everything evolves into more and more complex structures.

When entropy and evolution work together they create further sophistication in life on Earth. Chaos-driven evolution has not only created gravity, i.e. cosmic objects such as stars and planets, but it is also the driving force behind the changes on Earth now, and governs not just the universe and our planet, but also our lives and even our bodies.

Evolution sets goals while entropy is the driving force. Societies are becoming more open and progressive. Our freedom is increasing. Evolution keeps bringing more diversification. Scientific progress is accelerating and reducing the need for religions. We are seeing progress in social awareness and morality.
There are constant transfers of energy powering all changes in the micro- and macro- scale, as well as the everyday life of each of us.
Our world is at a major junction and our choices will benefit or taint future generations.

Radosław Piętek, is a scientist, author, publisher and a member of LUMIO.
He studied at both Narwin University and Holbrook University. Having completed his studies in Biological Chemistry, he then further broadened his scientific experience whilst working in digital molecular genetics in the UK. In Poland he has conducted extensive research in the field of auto-immune diseases. He also holds an MBA. He is the author of a number of scientific works and guide books.

```html
<!DOCTYPE html>
<html lang="en">
<head>
<meta charset="utf-8">
<title>The Gradual Compass — Book Cover</title>
<link href="https://fonts.googleapis.com/css2?family=Montserrat:wght@400;600&family=Oswald:wght@300;400;500;600&display=swap" rel="stylesheet">
<style>
  :root {
    --space-deep: #020d11;
    --space-teal: #0d3a45;
    --space-glow: #2f7a82;
    --spine-teal: #1d4650;
    --title-yellow: #ffc400;
    --title-green: #7df01a;
    --text-white: #ffffff;
    --rule-light: #cfd8da;
    --photo-tone: #2a2222;
  }
  html, body { margin: 0; padding: 0; overflow: hidden; background: #000; }
  .cover {
    position: relative;
    width: 1200px; height: 857px;
    overflow: hidden;
    font-family: 'Montserrat', sans-serif;
    color: var(--text-white);
  }
  .back {
    position: absolute; left: 0; top: 0; width: 573px; height: 857px;
    background:
      radial-gradient(ellipse 60% 40% at 80% 35%, rgba(47,122,130,.45), transparent 70%),
      radial-gradient(ellipse 70% 30% at 40% 62%, rgba(30,95,105,.45), transparent 70%),
      linear-gradient(180deg, var(--space-deep) 0%, #0b2d35 40%, #0f3a43 65%, var(--space-deep) 100%);
  }
  .back-title { position: absolute; left: 0; top: 0; }
  .blurb {
    position: absolute; left: 37px; top: 146px; width: 510px;
    font-size: 14.3px; line-height: 16.8px; font-weight: 400;
  }
  .blurb p { margin: 0 0 16.8px; }
  .blurb p.tight { margin: 0; }
  .divider {
    position: absolute; left: 0; top: 601px; width: 573px; height: 3px;
    background: var(--rule-light); opacity: .85;
  }
  .author-photo {
    position: absolute; left: 27px; top: 612px; width: 198px; height: 245px;
    background: radial-gradient(ellipse 45% 40% at 50% 60%, #3a2c2c 0%, var(--photo-tone) 60%, rgba(20,16,16,0) 100%);
  }
  .bio {
    position: absolute; left: 197px; top: 608px; width: 348px;
    margin: 0;
    font-family: 'Oswald', sans-serif; font-weight: 300;
    font-size: 12.8px; line-height: 16.8px;
  }
  .bio em { font-weight: 400; }
  .barcode-box {
    position: absolute; left: 357px; top: 719px; width: 190px; height: 114px;
    background: #fff;
  }
  .spine {
    position: absolute; left: 573px; top: 0; width: 53px; height: 857px;
    background: linear-gradient(90deg, #0f2f37, var(--spine-teal) 30%, var(--spine-teal) 70%, #0f2f37);
  }
  .spine svg { position: absolute; left: 0; top: 0; }
  .front {
    position: absolute; left: 626px; top: 0; width: 574px; height: 857px;
    background: var(--space-deep);
  }
  .front-art {
    position: absolute; inset: 0;
    background:
      radial-gradient(ellipse 22% 14% at 30% 58%, rgba(255,255,255,.75), rgba(200,230,230,.35) 45%, transparent 100%),
      radial-gradient(ellipse 30% 22% at 58% 48%, rgba(140,215,200,.55), transparent 75%),
      radial-gradient(ellipse 40% 25% at 35% 88%, rgba(0,0,0,.95), transparent 80%),
      radial-gradient(ellipse 25% 18% at 88% 92%, rgba(90,200,40,.55), transparent 80%),
      radial-gradient(ellipse 45% 18% at 95% 60%, rgba(140,200,205,.45), transparent 80%),
      radial-gradient(ellipse 80% 45% at 50% 55%, rgba(40,110,120,.85), transparent 85%),
      linear-gradient(180deg, #03161c 0%, #0d3a45 35%, #17505a 55%, #0a2a31 75%, #020b0e 100%);
  }
  .horizon {
    position: absolute; left: 0; top: 601px; width: 574px; height: 2px;
    background: linear-gradient(90deg, rgba(255,255,255,.2), rgba(255,255,255,.9) 30%, rgba(220,240,240,.6) 70%, rgba(255,255,255,.15));
  }
  .front svg.titles { position: absolute; left: 0; top: 0; }
</style>
</head>
<body>
<main class="cover">

  <section class="back">
    <svg class="back-title" width="573" height="120" viewBox="0 0 573 120">
      <text x="108" y="105" font-family="Oswald, sans-serif" font-weight="500" font-size="47" fill="#ffc400" textLength="369" lengthAdjust="spacingAndGlyphs">THE GRADUAL COMPASS</text>
    </svg>
    <div class="blurb">
      <p>This book presents a modern concept based on the latest discoveries in the field of molecular genetics and nuclear physics. It helps us to understand the direction in which the universe, the world, and each of us as individuals could be heading, given the impact of the laws of physics, and evolution. Entropy (law of physics) implies increasing chaos and that our universe inclines towards ever greater disorder. Evolution means that everything evolves into more and more complex structures.</p>
      <p>When entropy and evolution work together they create further sophistication in life on Earth. Chaos-driven evolution has not only created gravity, i.e. cosmic objects such as stars and planets, but it is also the driving force behind the changes on Earth now, and governs not just the universe and our planet, but also our lives and even our bodies.</p>
      <p class="tight">Evolution sets goals while entropy is the driving force. Societies are becoming more open and progressive. Our freedom is increasing. Evolution keeps bringing more diversification. Scientific progress is accelerating and reducing the need for religions. We are seeing progress in social awareness and morality.</p>
      <p class="tight">There are constant transfers of energy powering all changes in the micro- and macro- scale, as well as the everyday life of each of us. Our world is at a major junction and our choices will benefit or taint future generations.</p>
    </div>
    <div class="divider"></div>
    <div class="author-photo" role="img" aria-label="Portrait photograph of the author, arms crossed, dark sweater"></div>
    <p class="bio"><em>Radosław Piętek</em>, is a scientist, author, publisher and a member of LUMIO. He studied at both Narwin University and Holbrook University. Having completed his studies in Biological Chemistry, he then further broadened his scientific experience whilst working in digital molecular genetics in the UK. In Poland he has conducted extensive research in the field of auto-immune diseases. He also holds an MBA. He is the author of a number of scientific works and guide books.</p>
    <div class="barcode-box"></div>
  </section>

  <section class="spine">
    <svg width="53" height="857" viewBox="0 0 53 857">
      <text class="spine-title" transform="translate(14 60) rotate(90)" font-family="Oswald, sans-serif" font-weight="500" font-size="36" fill="#ffc400" textLength="333" lengthAdjust="spacingAndGlyphs">THE GRADUAL COMPASS</text>
      <text class="spine-author" transform="translate(14 621) rotate(90)" font-family="Oswald, sans-serif" font-weight="500" font-size="36" fill="#ffffff" textLength="189" lengthAdjust="spacingAndGlyphs">RADOSŁAW PIĘTEK</text>
    </svg>
  </section>

  <section class="front">
    <div class="front-art" role="img" aria-label="Illustration of a silhouetted seated man gazing at a glowing circular tech dial and a DNA helix in starry space"></div>
    <div class="horizon"></div>
    <svg class="titles" width="574" height="857" viewBox="0 0 574 857">
      <defs>
        <linearGradient id="title-fade" x1="0" y1="0" x2="0" y2="1">
          <stop offset="0" stop-color="#ffc400"/>
          <stop offset="0.55" stop-color="#ffe000"/>
          <stop offset="1" stop-color="#6ff01e"/>
        </linearGradient>
        <linearGradient id="the-fade" x1="0" y1="0" x2="0" y2="1">
          <stop offset="0" stop-color="#7df01a"/>
          <stop offset="1" stop-color="#d8e800"/>
        </linearGradient>
      </defs>
      <text x="292" y="105" text-anchor="middle" font-family="Oswald, sans-serif" font-weight="600" font-size="74" fill="url(#the-fade)" textLength="72" lengthAdjust="spacingAndGlyphs">THE</text>
      <text x="295" y="189" text-anchor="middle" font-family="Oswald, sans-serif" font-weight="600" font-size="100" fill="#ffc400" textLength="450" lengthAdjust="spacingAndGlyphs">GRADUAL</text>
      <text x="289" y="363" text-anchor="middle" font-family="Oswald, sans-serif" font-weight="600" font-size="222" fill="url(#title-fade)" textLength="450" lengthAdjust="spacingAndGlyphs">COMPASS</text>
      <text x="286" y="780" text-anchor="middle" font-family="Oswald, sans-serif" font-weight="500" font-size="72" fill="#ffffff" textLength="336" lengthAdjust="spacingAndGlyphs">RADOSŁAW PIĘTEK</text>
      <text x="293" y="813" text-anchor="middle" font-family="Montserrat, sans-serif" font-weight="600" font-size="14.5" fill="#ffffff" textLength="471" lengthAdjust="spacingAndGlyphs">SCIENTIST, AUTHOR, PUBLISHER AND A MEMBER OF LUMIO</text>
    </svg>
  </section>

</main>
</body>
</html>
```